Venue Booking Site

I would like a venue directory and booking website designed. The idea is that end users will come to the site to find venues for weddings, parties, events etc. They will be able to find the venue based on many criteria, the most important ones are availability and location - they will be able to see in real time which venues are available for the desired dates and areas.

Venues will be able to use the website as a reservation management tool, receive payments for bookings through the site and be able to manage bookings on the go. This will be made into an app. It needs to be developed in bootstrap. Brand name to be used: Pinevault. Venue, place and space bookings.

Target audience - end users - anyone who is looking for a venue. For Community members it will provide an easy way to find a suitable venue
Outline what dates and times the venue is available
Outline costs involved in booking the venue
Search via many other criteria
It will allow the customer to book and pay for the venue online in one smooth process

Clients: Venue managers - particularly focussing on not for profit businesses eg, GPWs, community hall managers, small business managers. These people typically use paper based systems yet and do not use websites so it needs to be very user friendly. Future growth to restaurants, pubs, event venues who have a stronger familiarity with computers and who might already use their own booking management tool - so this needs to be able to link in with their system.

What need will this meet for venue managers:
This tool provides venues with greater visibility, promotion and advertising of their venue
This allows more customers to find them and book with them
This tool will be offered to not-for-profit venue managers for free to better connect them to the community
This means greater profit for these community venues
This means more revenue and jobs created in these communities

Sample of the layout / contents attached. This is not a complete site map as yet as it is a work in progress for final pages.

Industry/Entity Type

Small Business

Number of Pages Required

5+ page

Font styles to use
Sans Serif

Colors
eb2027

Requirements
Must have
• This is a psd file only - one template for each different section, home page, search page, detailed page view, admin back end
Should not have
• does not need to be coded.
• Note, the lantern quay logo jpeg files were files we were toying with using for this project- but I am happy to use the main pinevault logo- I will let you decide.

```html
<!DOCTYPE html>
<html lang="en">
<head>
<meta charset="utf-8">
<title>Pinevault – Venue Booking</title>
<link href="https://fonts.googleapis.com/css2?family=Open+Sans:wght@300;400;600;700&display=swap" rel="stylesheet">
<style>
:root{
  --red:#eb2027;
  --red-dark:#c8161c;
  --ink:#333;
  --muted:#666;
  --line:#e2e2e2;
  --panel:#f4f4f4;
  --nav-top:#5a5a5a;
  --nav-bottom:#3c3c3c;
  --footer:#505050;
  --footer-deep:#3d3d3d;
  --star:#f26522;
}
*{box-sizing:border-box;margin:0;padding:0}
html,body{width:1200px;height:2195px;overflow:hidden}
body{font-family:"Open Sans",Arial,sans-serif;color:var(--ink);background:#fff;position:relative}
.abs{position:absolute}

/* header */
.brand{left:100px;top:30px}
.brand-name{font-size:42px;font-weight:600;color:var(--red);line-height:1;display:flex;align-items:center;gap:10px}
.brand-name .dot{width:14px;height:14px;background:var(--red);display:inline-block}
.brand-tag{font-size:14px;color:#666;margin-top:8px;padding-left:24px}
.list-venue{left:522px;top:23px;width:118px;height:30px;border-radius:15px;background:#8a8a8a;color:#fff;font-size:12px;display:flex;align-items:center;justify-content:center}
.login-label{left:648px;top:24px;font-size:20px;font-weight:600;color:#444}
.field{border:1px solid #ddd;border-radius:16px;background:#fff;font-size:12px;color:#999;display:flex;align-items:center;padding-left:16px}
.login-btn{left:1045px;top:23px;width:53px;height:30px;border-radius:15px;background:var(--red);color:#fff;font-size:13px;display:flex;align-items:center;justify-content:center}
.support{left:606px;top:74px;text-align:right;width:118px}
.support small{display:block;font-size:12px;color:#777}
.support strong{font-size:20px;color:var(--red);font-weight:600;line-height:1.1}
.sep{left:790px;top:74px;width:1px;height:38px;background:#e5e5e5}

/* nav */
.main-nav{left:0;top:142px;width:1200px;height:51px;background:linear-gradient(var(--nav-top),var(--nav-bottom));display:flex;padding-left:101px}
.main-nav a{color:#fff;text-decoration:none;font-size:14px;letter-spacing:.5px;display:flex;align-items:center;justify-content:center;border-right:1px solid #2f2f2f;box-shadow:inset -1px 0 0 #666}
.main-nav a.active{background:var(--red)}

/* map */
.map{left:0;top:193px;width:1200px;height:607px;background:linear-gradient(135deg,#ebe7df 0%,#e4e0d7 55%,#d8e3ee 75%,#b9d1ea 100%)}
.pin-card{width:170px;height:76px;background:#fff;border-radius:8px;border:2px solid var(--red);box-shadow:0 3px 6px rgba(0,0,0,.25);display:flex;gap:6px;padding:6px}
.pin-card::after{content:"";position:absolute;right:34px;bottom:-13px;border:7px solid transparent;border-top-color:#fff;border-left-color:#fff}
.pin-thumb{width:60px;height:60px;border-radius:4px;background:linear-gradient(#7a8fb0,#8a6848)}
.pin-body h4{font-size:13px;font-weight:400;color:#555}
.pin-body p{font-size:7px;color:#999;line-height:1.3}
.pin-body .stars{font-size:13px}
.stars{color:var(--star);letter-spacing:1px}

/* search panel */
.finder{left:0;top:800px;width:1200px;height:272px;background:var(--panel)}
.finder-col h2{font-size:42px;font-weight:300;color:var(--red);line-height:1}
.finder-col label{display:block;font-size:14px;color:#555;margin-top:30px}
.check{display:flex;align-items:center;gap:10px;font-size:14px;color:#666;height:34px}
.check i{width:16px;height:16px;border:1px solid #ccc;background:#fff;display:inline-block}
.check i.on{background:#eaeaea}
.divider-v{width:1px;height:230px;top:820px;background:#dedede}
.input{position:absolute;height:35px;border:1px solid #ddd;border-radius:18px;background:#fff;font-size:13px;color:#999;display:flex;align-items:center;justify-content:space-between;padding:0 16px}
.redline{left:0;top:1072px;width:1200px;height:4px;background:var(--red)}
.search-tab{left:516px;top:1072px;width:167px;height:40px;background:var(--red);border-radius:0 0 40px 40px;color:#fff;font-size:22px;font-weight:700;letter-spacing:1px;display:flex;align-items:center;justify-content:center}

/* venues */
.section-title{left:0;width:1200px;text-align:center;color:var(--red);font-weight:300;font-size:38px}
.venue-card{top:1203px;width:225px;height:364px;background:#f5f5f5;text-align:center}
.venue-photo{height:141px}
.venue-card h3{font-size:15px;font-weight:400;color:var(--red);margin-top:24px}
.venue-card .city{font-size:13px;color:#555;margin-top:4px}
.venue-card .stars{font-size:16px;margin-top:2px}
.venue-card p{font-size:12px;color:#666;line-height:1.55;padding:0 15px;margin-top:6px}
.book-btn{display:inline-block;margin-top:14px;background:var(--red);color:#fff;font-size:12px;padding:5px 13px;border-radius:14px}
.rule{left:100px;top:1602px;width:1000px;height:1px;background:#ddd}

/* benefits */
.benefit{display:flex;align-items:center;gap:16px;font-size:19px;color:#444}
.benefit svg{width:30px;height:30px}

/* footer */
.footer{left:0;top:1851px;width:1200px;height:238px;background:var(--footer);color:#eee}
.foot-brand{left:100px;top:1885px}
.foot-brand .brand-name{color:#d0d0d0}
.foot-brand .dot{background:#d0d0d0}
.foot-brand .brand-tag{color:#bbb}
.foot-contact{left:103px;top:1986px;font-size:13px;line-height:25px;color:#e6e6e6}
.foot-head{font-size:16px;color:#fff}
.foot-list{list-style:none;font-size:12px;color:#ddd;line-height:25px;margin-top:8px}
.foot-list li::before{content:"• ";color:#bbb}
.social{display:grid;grid-template-columns:repeat(3,45px);gap:2px 3px;margin-top:16px}
.social span{width:45px;height:45px;border-radius:50%;background:#fff;display:block}
.email-box{left:859px;top:1924px;width:193px;height:38px;background:#d7d7d7;font-size:13px;color:#666;display:flex;align-items:center;padding-left:14px}
.email-go{left:1052px;top:1924px;width:39px;height:38px;background:#8a8a8a;display:flex;align-items:center;justify-content:center}
.bottom-bar{left:0;top:2089px;width:1200px;height:106px;background:var(--footer-deep);text-align:center;color:#ddd}
.bottom-links{font-size:13px;margin-top:26px;word-spacing:2px}
.bottom-links span{color:#888;margin:0 8px}
.copyright{font-size:12px;margin-top:12px}
</style>
</head>
<body>

<header>
  <div class="abs brand">
    <div class="brand-name"><span class="dot"></span>pinevault</div>
    <div class="brand-tag">Venue Booking</div>
  </div>
  <div class="abs list-venue">List My Venue</div>
  <div class="abs login-label">Login</div>
  <div class="abs field" style="left:710px;top:23px;width:156px;height:30px">Username</div>
  <div class="abs field" style="left:878px;top:23px;width:158px;height:30px">********</div>
  <div class="abs login-btn">Login</div>

  <svg class="abs" style="left:524px;top:82px" width="28" height="26" viewBox="0 0 28 26" aria-hidden="true">
    <path d="M14 2 L27 14 H23 V25 H17 V17 H11 V25 H5 V14 H1 Z" fill="#bdbdbd"/>
  </svg>
  <div class="abs support"><small>24/7 Support</small><strong>555 214 7730</strong></div>
  <svg class="abs" style="left:730px;top:76px" width="36" height="36" viewBox="0 0 36 36" aria-hidden="true">
    <circle cx="18" cy="18" r="18" fill="#bdbdbd"/>
    <path d="M12 10 l4 0 l2 5 l-3 2 a11 11 0 0 0 5 5 l2 -3 l5 2 l0 4 a3 3 0 0 1 -3 2 a17 17 0 0 1 -15 -15 a3 3 0 0 1 3 -2z" fill="#fff"/>
  </svg>
  <div class="abs sep"></div>
  <div class="abs field" style="left:815px;top:75px;width:283px;height:36px;justify-content:space-between;padding-right:14px">Search
    <svg width="16" height="16" viewBox="0 0 16 16" aria-hidden="true"><circle cx="6.5" cy="6.5" r="5" fill="none" stroke="#999" stroke-width="1.6"/><line x1="10.5" y1="10.5" x2="15" y2="15" stroke="#999" stroke-width="1.8"/></svg>
  </div>
</header>

<nav class="abs main-nav">
  <a class="active" style="width:120px">HOME</a>
  <a style="width:137px">VENUES</a>
  <a style="width:186px">NEWS &amp; OFFERS</a>
  <a style="width:171px">INSPIRATION</a>
  <a style="width:136px">SERVICES</a>
  <a style="width:134px">CONTACT</a>
  <a style="width:114px;border-right:none;box-shadow:none">FAQS</a>
</nav>

<div class="abs map" role="img" aria-label="Street map of the city with canals and venue markers"></div>
<div class="abs pin-card" style="left:281px;top:414px"><div class="pin-thumb"></div><div class="pin-body"><h4>Aenean sed</h4><p>Nulla tincidunt rhoncus tellus urna</p><div class="stars">★★★★★</div></div></div>
<div class="abs pin-card" style="left:616px;top:414px"><div class="pin-thumb"></div><div class="pin-body"><h4>Aenean sed</h4><p>Nulla tincidunt rhoncus tellus urna</p><div class="stars">★★★★★</div></div></div>
<div class="abs pin-card" style="left:636px;top:546px"><div class="pin-thumb"></div><div class="pin-body"><h4>Aenean sed</h4><p>Nulla tincidunt rhoncus tellus urna</p><div class="stars">★★★★★</div></div></div>
<div class="abs pin-card" style="left:936px;top:568px"><div class="pin-thumb"></div><div class="pin-body"><h4>Aenean sed</h4><p>Nulla tincidunt rhoncus tellus urna</p><div class="stars">★★★★★</div></div></div>

<section class="abs finder"></section>
<div class="abs finder-col" style="left:165px;top:830px">
  <h2>What</h2>
  <div style="margin-top:14px">
    <div class="check"><i class="on"></i>Hotel</div>
    <div class="check"><i></i>Restaurant</div>
    <div class="check"><i></i>Self Catering</div>
    <div class="check"><i></i>Rent a Car</div>
    <div class="check"><i></i>Tour</div>
  </div>
</div>
<div class="abs divider-v" style="left:348px"></div>
<div class="abs finder-col" style="left:370px;top:830px;width:210px"><h2>Where</h2><label style="margin-top:22px">Your destination</label></div>
<div class="input" style="left:370px;top:917px;width:209px">City, region, district</div>
<div class="abs divider-v" style="left:600px"></div>
<div class="abs finder-col" style="left:623px;top:830px"><h2>When</h2><label style="margin-top:22px">Check-in date</label></div>
<div class="input" style="left:623px;top:917px;width:209px">dd/mm/yyyy
  <svg width="20" height="18" viewBox="0 0 20 18" aria-hidden="true"><rect x="1" y="2" width="18" height="15" fill="none" stroke="#888"/><path d="M1 6 H19 M5 9 H7 M9 9 H11 M13 9 H15 M5 12 H7 M9 12 H11 M13 12 H15" stroke="#888"/></svg></div>
<div class="abs" style="left:623px;top:975px;font-size:14px;color:#555">Check-out date</div>
<div class="input" style="left:623px;top:1002px;width:209px">dd/mm/yyyy
  <svg width="20" height="18" viewBox="0 0 20 18" aria-hidden="true"><rect x="1" y="2" width="18" height="15" fill="none" stroke="#888"/><path d="M1 6 H19 M5 9 H7 M9 9 H11 M13 9 H15 M5 12 H7 M9 12 H11 M13 12 H15" stroke="#888"/></svg></div>
<div class="abs divider-v" style="left:849px"></div>
<div class="abs finder-col" style="left:873px;top:830px"><h2>Who</h2><label style="margin-top:22px">Rooms</label></div>
<div class="input" style="left:873px;top:917px;width:210px">dd/mm/yyyy
  <svg width="10" height="14" viewBox="0 0 10 14" aria-hidden="true"><path d="M5 1 L9 5 H1Z M5 13 L9 9 H1Z" fill="#777"/></svg></div>
<div class="abs redline"></div>
<div class="abs search-tab">SEARCH</div>

<h2 class="abs section-title" style="top:1138px">Top Venues</h2>

<article class="abs venue-card" style="left:111px">
  <div class="venue-photo" role="img" aria-label="Canal-side hotel with moored boats" style="background:linear-gradient(#9fb3c8,#6d5a44 60%,#3e4a4f)"></div>
  <h3>Aenean sed tempor</h3><div class="city">London</div><div class="stars">★★★★★</div>
  <p>Morbi ullamcorper ultrices arcu, blandit dignissim metus aliquam eu. Vestibulum ante ipsum primis in faucibus orci luctus.</p>
  <span class="book-btn">Book Now</span>
</article>
<article class="abs venue-card" style="left:361px">
  <div class="venue-photo" role="img" aria-label="Elegant hotel suite interior" style="background:linear-gradient(#d9d4c8,#7b6e5c 70%,#3a3530)"></div>
  <h3>Aenean sed tempor</h3><div class="city">London</div><div class="stars">★★★★★</div>
  <p>Morbi ullamcorper ultrices arcu, blandit dignissim metus aliquam eu. Vestibulum ante ipsum primis in faucibus orci luctus.</p>
  <span class="book-btn">Book Now</span>
</article>
<article class="abs venue-card" style="left:612px">
  <div class="venue-photo" role="img" aria-label="Indoor canal venue with gondola" style="background:linear-gradient(#b8c6d6,#9a7f5e 55%,#1f4a6e)"></div>
  <h3>Aenean sed tempor</h3><div class="city">London</div><div class="stars">★★★★★</div>
  <p>Morbi ullamcorper ultrices arcu, blandit dignissim metus aliquam eu. Vestibulum ante ipsum primis in faucibus orci luctus.</p>
  <span class="book-btn">Book Now</span>
</article>
<article class="abs venue-card" style="left:863px">
  <div class="venue-photo" role="img" aria-label="Warmly lit restaurant dining room" style="background:linear-gradient(#6b3a1e,#3b2012 60%,#1c100a)"></div>
  <h3>Aenean sed tempor</h3><div class="city">London</div><div class="stars">★★★★★</div>
  <p>Morbi ullamcorper ultrices arcu, blandit dignissim metus aliquam eu. Vestibulum ante ipsum primis in faucibus orci luctus.</p>
  <span class="book-btn">Book Now</span>
</article>

<div class="abs rule"></div>
<h2 class="abs section-title" style="top:1638px">Why should you book your venue through Pinevault</h2>

<div class="abs benefit" style="left:138px;top:1714px">
  <svg viewBox="0 0 30 30" aria-hidden="true"><rect x="3" y="8" width="12" height="20" fill="none" stroke="#777" stroke-width="2"/><rect x="15" y="3" width="12" height="25" fill="none" stroke="#777" stroke-width="2"/><path d="M6 12h2M10 12h2M6 17h2M10 17h2M6 22h2M10 22h2M18 8h2M22 8h2M18 13h2M22 13h2M18 18h2M22 18h2" stroke="#777" stroke-width="2"/></svg>Handpicked Hotels</div>
<div class="abs benefit" style="left:475px;top:1714px">
  <svg viewBox="0 0 30 30" aria-hidden="true"><path d="M7 3h12l5 5v19H7z" fill="#777"/><path d="M19 3v5h5" fill="#aaa"/></svg>Detailed Description</div>
<div class="abs benefit" style="left:805px;top:1714px">
  <svg viewBox="0 0 30 30" aria-hidden="true"><circle cx="15" cy="6" r="3" fill="#777"/><path d="M15 10v9M9 14h12M15 19l-5 8M15 19l5 8" stroke="#777" stroke-width="2" fill="none"/></svg>Exclusive Knowledge</div>
<div class="abs benefit" style="left:138px;top:1777px">
  <svg viewBox="0 0 30 30" aria-hidden="true"><rect x="2" y="10" width="26" height="12" fill="none" stroke="#777" stroke-width="2"/><path d="M8 10v12M14 10v12" stroke="#777" stroke-width="2"/></svg>Best Price Guarantee</div>
<div class="abs benefit" style="left:475px;top:1777px">
  <svg viewBox="0 0 30 30" aria-hidden="true"><path d="M9 13V9a6 6 0 0 1 12 0v4" fill="none" stroke="#777" stroke-width="3"/><rect x="6" y="13" width="18" height="14" fill="#777"/></svg>Secure Booking</div>
<div class="abs benefit" style="left:805px;top:1777px">
  <svg viewBox="0 0 30 30" aria-hidden="true"><circle cx="15" cy="15" r="12" fill="#777"/><circle cx="15" cy="15" r="5" fill="#fff"/><path d="M6 10l5 3M24 10l-5 3M6 20l5-3M24 20l-5-3" stroke="#fff" stroke-width="3"/></svg>Best Customer support</div>

<footer>
  <div class="abs footer"></div>
  <div class="abs brand foot-brand">
    <div class="brand-name"><span class="dot"></span>pinevault</div>
    <div class="brand-tag">Venue Booking</div>
  </div>
  <div class="abs foot-contact">12 Larchmere Crt Ashdale VIC<br>P: 03 5550 1842<br>E: info@bookings.pinevault.com.au</div>
  <div class="abs" style="left:382px;top:1882px">
    <div class="foot-head">Customer Support</div>
    <ul class="foot-list"><li>FAQ</li><li>How do i make a reservation?</li><li>Payment Option</li><li>Booking tips</li></ul>
  </div>
  <div class="abs" style="left:662px;top:1882px">
    <div class="foot-head">Follow us on</div>
    <div class="social"><span></span><span></span><span></span><span></span><span></span><span></span></div>
  </div>
  <div class="abs foot-head" style="left:856px;top:1882px">Don't miss our exclusive offers</div>
  <div class="abs email-box">E-mail ID</div>
  <div class="abs email-go"><svg width="18" height="18" viewBox="0 0 18 18" aria-hidden="true"><path d="M2 9h12M9 3l6 6-6 6" stroke="#fff" stroke-width="3" fill="none"/></svg></div>
  <div class="abs bottom-bar">
    <div class="bottom-links">Home<span>|</span>Venues<span>|</span>News &amp; Offers<span>|</span>Inspiration<span>|</span>Services<span>|</span>Contact<span>|</span>FAQs</div>
    <div class="copyright">Copyright © 2014 Pinevault. All rights reserved.</div>
  </div>
</footer>

</body>
</html>
```